Walkup Playtime Arcade Poster

We need a A2 Poster designed to advertise our Walkup Playtime Arcade Kiosks in food courts. This poster to be placed in locations where people queue for food or coffee. Poster should be able to be scaled down to an A4 size and printed on vinyl to be stuck onto food court tables. Poster should be able to be scaled down to A5 for placement into perspex menu holders to sit on tables. I have uploaded a mockup showing the wording required.

Target Market(s)

Food Courts/High Traffic Areas

Industry/Entity Type

Retail

Requirements
Must have
• Poster must stand out and be eye catching.

```html
<!DOCTYPE html>
<html lang="en">
<head>
<meta charset="utf-8">
<title>Walkup Playtime Arcade Poster</title>
<link rel="stylesheet" href="https://fonts.googleapis.com/css2?family=Oswald:wght@500;700&family=Roboto:wght@400;700&display=swap">
<style>
  :root {
    --charcoal: #1f1f21;
    --charcoal-soft: #2c2c2f;
    --blue: #1e7fe0;
    --blue-deep: #1560b8;
    --white: #ffffff;
    --grey-light: #d8d8d8;
    --kiosk-dark: #262628;
    --kiosk-mid: #4a4b50;
  }
  * { margin: 0; padding: 0; box-sizing: border-box; }
  html, body { width: 900px; height: 1200px; overflow: hidden; background: var(--charcoal); }
  .poster {
    position: relative; width: 900px; height: 1200px; overflow: hidden;
    background: radial-gradient(ellipse at 70% 40%, var(--charcoal-soft), var(--charcoal) 70%);
    font-family: "Roboto", Arial, sans-serif; color: var(--white);
  }
  .backdrop { position: absolute; inset: 0; }
  .brand {
    position: absolute; top: 52px; right: 40px;
    display: flex; align-items: center; gap: 18px;
  }
  .brand-square { width: 96px; height: 96px; background: var(--blue); }
  .brand-name {
    font-family: "Oswald", Arial, sans-serif; font-weight: 700;
    font-size: 46px; line-height: 1.05; letter-spacing: 1px; text-transform: uppercase;
    color: var(--white);
  }
  .kiosk-art {
    position: absolute; left: 140px; top: 170px; width: 240px; height: 720px;
    background: linear-gradient(160deg, var(--kiosk-mid), var(--kiosk-dark) 60%);
    border-radius: 22px 22px 6px 6px;
  }
  .headline {
    position: absolute; right: 40px; top: 280px; width: 340px; text-align: right;
    font-family: "Oswald", Arial, sans-serif; font-weight: 700; text-transform: uppercase;
    font-size: 56px; line-height: 1.12;
  }
  .headline .accent { color: var(--blue); }
  .connect {
    position: absolute; right: 40px; top: 640px; width: 360px; text-align: right;
    font-family: "Oswald", Arial, sans-serif; font-weight: 700;
  }
  .connect-title { font-size: 48px; line-height: 1.15; text-transform: uppercase; }
  .connect-title .wifi { text-transform: none; }
  .network-name { font-size: 22px; color: var(--blue); margin-top: 8px; letter-spacing: 0.5px; }
  .features { position: absolute; right: 40px; top: 830px; list-style: none; text-align: right; }
  .features li {
    font-size: 21px; color: var(--grey-light); margin-bottom: 26px;
    display: flex; align-items: center; justify-content: flex-end; gap: 18px;
  }
  .features li::after {
    content: ""; border-top: 11px solid transparent; border-bottom: 11px solid transparent;
    border-right: 20px solid var(--white);
  }
  .network-note {
    position: absolute; left: 40px; right: 40px; top: 1040px;
    font-weight: 700; font-size: 19px;
  }
  .network-note .accent { color: var(--blue); }
  .availability {
    position: absolute; left: 0; right: 0; bottom: 0; height: 100px;
    background: var(--charcoal);
    display: flex; align-items: center; justify-content: center;
    font-weight: 700; font-size: 24px; letter-spacing: 3px; text-transform: uppercase; color: var(--grey-light);
  }
</style>
</head>
<body>
<main class="poster">
  <svg class="backdrop" width="900" height="1200" viewBox="0 0 900 1200" aria-hidden="true">
    <polygon points="0,120 0,560 380,340 200,120" fill="var(--blue)"/>
    <polygon points="0,620 0,1010 300,1010 120,620" fill="var(--blue-deep)"/>
    <path d="M60,330 L590,610 Q610,620 590,632 L60,900 Q30,915 30,880 L30,350 Q30,315 60,330 Z" fill="var(--white)"/>
    <polygon points="520,930 900,930 900,1010 440,1010" fill="#3a3a3d"/>
  </svg>

  <div class="brand">
    <span class="brand-square"></span>
    <span class="brand-name">Walkup Playtime<br>Arcade</span>
  </div>

  <div class="kiosk-art" role="img" aria-label="Free-standing media kiosk with a touch screen"></div>

  <h1 class="headline">Watch movies <span class="accent">on your</span> smartphone or tablet</h1>

  <section class="connect">
    <h2 class="connect-title">Connect to<br>the free <span class="wifi">Wifi</span></h2>
    <p class="network-name">'WALKUP_PLAYTIME_ARCADE'</p>
  </section>

  <ul class="features">
    <li>Download movies in under 3 minutes</li>
    <li>No Internet Connection Required</li>
  </ul>

  <p class="network-note">Connect your portable device to the Free WiFi network <span class="accent">'WALKUP PLAYTIME ARCADE'</span></p>

  <footer class="availability">Available while sitting here'</footer>
</main>
</body>
</html>
```